Business Card for Cedar Ridge Home Inspections

Very professional card that has the same logo as in logo project with simple info listed below.

Colors are Black, Red, White Silver and Gold

Reason: The extension is to run concurrently with the logo project.

Target Market(s)

Real Estate Industry Professionals

Industry/Entity Type

Business

Font styles to use
Serif

Requirements
Must have
• Logo only on front.
Company name , inspector name, company website, company phone on bck

```html
<!DOCTYPE html>
<html lang="en">
<head>
<meta charset="utf-8">
<title>Cedar Ridge Home Inspections – Business Card</title>
<link rel="stylesheet" href="https://fonts.googleapis.com/css2?family=Oswald:wght@700&family=Questrial&display=swap">
<style>
  :root {
    --backdrop: #e9e9ea;
    --card-white: #fbfbfb;
    --card-black-top: #555657;
    --card-black-bottom: #151515;
    --ink-grey: #5d5d5f;
    --ink-light: #8a8a8c;
    --brand-red: #d9625c;
    --band-red: #d66a66;
    --band-dark: #3d3d3f;
    --band-silver: #b9b9bb;
    --band-gold: #d9ad3e;
    --rule: #c9c9cb;
    --logo-white: #f1f1f1;
  }
  * { box-sizing: border-box; margin: 0; padding: 0; }
  html, body { width: 1200px; height: 720px; overflow: hidden; }
  body {
    background: var(--backdrop);
    font-family: "Questrial", sans-serif;
    display: flex;
    align-items: center;
    justify-content: center;
    gap: 40px;
  }
  .card {
    position: relative;
    width: 540px;
    height: 308px;
    overflow: hidden;
    box-shadow: 0 6px 18px rgba(0,0,0,0.12);
  }
  .card--front { background: var(--card-white); }
  .card--back {
    background: linear-gradient(160deg, var(--card-black-top), var(--card-black-bottom));
    display: flex;
    align-items: center;
    justify-content: center;
  }

  .colour-bar {
    position: absolute;
    left: 0; right: 0; bottom: 0;
    display: flex;
    flex-direction: column;
  }
  .colour-bar span { display: block; height: 6px; }
  .colour-bar .red { background: var(--band-red); }
  .colour-bar .dark { background: var(--band-dark); }
  .colour-bar .silver { background: var(--band-silver); }
  .colour-bar .gold { background: var(--band-gold); }

  .brand {
    position: absolute;
    display: flex;
    align-items: center;
    gap: 10px;
  }
  .brand__dot {
    width: 16px; height: 16px;
    border-radius: 50%;
    border: 3px solid currentColor;
    flex: none;
  }
  .brand__name { line-height: 1.05; font-weight: 400; }
  .brand__name span { display: block; }

  .card--front .brand { left: 26px; top: 108px; color: var(--ink-grey); }
  .card--front .brand__name { font-size: 30px; }
  .card--front .brand__name span + span { font-size: 15.5px; letter-spacing: 0.4px; text-transform: uppercase; }

  .card--back .brand { position: static; color: var(--logo-white); gap: 14px; }
  .card--back .brand__dot { width: 26px; height: 26px; border-width: 4px; }
  .card--back .brand__name { font-size: 52px; }
  .card--back .brand__name span + span { font-size: 26px; letter-spacing: 0.6px; text-transform: uppercase; }

  .divider {
    position: absolute;
    left: 258px; top: 70px;
    width: 2px; height: 140px;
    background: var(--rule);
  }
  .contact {
    position: absolute;
    left: 282px; top: 70px;
    color: var(--ink-light);
  }
  .contact__name {
    font-family: "Oswald", sans-serif;
    font-weight: 700;
    font-size: 27px;
    color: var(--ink-grey);
    line-height: 1.1;
  }
  .contact__role { font-size: 13px; color: var(--brand-red); margin-bottom: 14px; }
  .contact__line {
    display: flex; align-items: center; gap: 10px;
    font-size: 15px; margin-bottom: 10px;
  }
  .contact__line svg { width: 16px; height: 16px; flex: none; }
</style>
</head>
<body>
  <section class="card card--front" aria-label="Card front">
    <div class="brand">
      <span class="brand__dot"></span>
      <p class="brand__name"><span>Cedar Ridge</span><span>Home Inspections</span></p>
    </div>

    <div class="divider"></div>

    <div class="contact">
      <p class="contact__name">Daniel Reyes</p>
      <p class="contact__role">Inspector</p>
      <p class="contact__line">
        <svg viewBox="0 0 24 24"><path fill="var(--brand-red)" d="M6.6 10.8a15 15 0 0 0 6.6 6.6l2.2-2.2a1 1 0 0 1 1-.25 11.4 11.4 0 0 0 3.6.57 1 1 0 0 1 1 1V20a1 1 0 0 1-1 1A17 17 0 0 1 3 4a1 1 0 0 1 1-1h3.5a1 1 0 0 1 1 1c0 1.25.2 2.45.57 3.6a1 1 0 0 1-.25 1z"/></svg>
        555-014-2273
      </p>
      <p class="contact__line">
        <svg viewBox="0 0 24 24" fill="none" stroke="var(--brand-red)" stroke-width="2"><rect x="2" y="5" width="20" height="14"/><path d="M2 5l10 8 10-8"/></svg>
        hello@cedarridgehi.com
      </p>
    </div>

    <div class="colour-bar" aria-hidden="true">
      <span class="red"></span>
      <span class="dark"></span>
      <span class="silver"></span>
      <span class="gold"></span>
    </div>
  </section>

  <section class="card card--back" aria-label="Card back">
    <div class="brand">
      <span class="brand__dot"></span>
      <p class="brand__name"><span>Cedar Ridge</span><span>Home Inspections</span></p>
    </div>
  </section>
</body>
</html>
```